Business Card for New Business

Please design a business card using our logo and font files. This is only one card for one person, as listed in details section.

Industry/Entity Type

Business

Contact Information for Business Card

Carl Voserby

Phone 240.318.6624
Cell 703.581.4096
Email carl@moltravex.com

www.moltravex.com

Address
18250 Brennick Lane #314
Damascus, MD 20715

Font styles to use
Sans Serif

Requirements
Must have
• Information listed in detail section. Must be standard card size.

```html
<!DOCTYPE html>
<html lang="en">
<head>
<meta charset="utf-8">
<title>Carl Voserby – Business Card</title>
<link rel="stylesheet" href="https://fonts.googleapis.com/css2?family=Quicksand:wght@400;500;700&display=swap">
<style>
  :root {
    --backdrop: #e4e5e3;
    --card-red: #a43a31;
    --ink-cream: #e8d3bd;
    --ink-soft: #dcbfa6;
    --rule: #c98a74;
  }
  html, body {
    margin: 0;
    padding: 0;
    width: 1200px;
    height: 1000px;
    overflow: hidden;
    background: var(--backdrop);
  }
  .canvas {
    width: 1200px;
    height: 1000px;
    display: flex;
    align-items: center;
    justify-content: center;
  }
  .card {
    width: 480px;
    height: 840px;
    background: var(--card-red);
    color: var(--ink-cream);
    font-family: "Quicksand", sans-serif;
    box-sizing: border-box;
    position: relative;
    text-align: center;
    box-shadow: 0 12px 30px rgba(0,0,0,0.12);
  }
  .brand {
    position: absolute;
    top: 92px;
    left: 0;
    right: 0;
    display: flex;
    align-items: center;
    justify-content: center;
    gap: 10px;
    font-weight: 500;
    font-size: 46px;
    letter-spacing: 1px;
  }
  .brand-dot {
    width: 36px;
    height: 36px;
    border-radius: 50%;
    background: var(--ink-cream);
  }
  .person-name {
    position: absolute;
    top: 218px;
    left: 0;
    right: 0;
    margin: 0;
    font-weight: 700;
    font-size: 30px;
    letter-spacing: 0.5px;
  }
  .address {
    position: absolute;
    top: 318px;
    left: 0;
    right: 0;
    margin: 0;
    font-style: normal;
    font-size: 19px;
    line-height: 32px;
    letter-spacing: 1px;
    color: var(--ink-soft);
  }
  .divider {
    position: absolute;
    top: 414px;
    left: 110px;
    width: 260px;
    height: 1px;
    background: var(--rule);
  }
  .contacts {
    position: absolute;
    top: 520px;
    left: 120px;
    margin: 0;
    padding: 0;
    list-style: none;
    text-align: left;
    font-size: 19px;
    letter-spacing: 1.5px;
    color: var(--ink-soft);
  }
  .contacts li {
    display: flex;
    align-items: center;
    gap: 20px;
    height: 34px;
  }
  .contacts svg {
    width: 16px;
    height: 16px;
    flex: none;
  }
  .website {
    position: absolute;
    bottom: 78px;
    left: 0;
    right: 0;
    margin: 0;
    font-weight: 700;
    font-size: 15px;
    letter-spacing: 3px;
    color: var(--ink-soft);
  }
</style>
</head>
<body>
<main class="canvas">
  <article class="card">
    <div class="brand"><span class="brand-dot"></span><span class="brand-name">moltravex</span></div>

    <h1 class="person-name">Carl Voserby</h1>

    <address class="address">18250 Brennick Lane #314<br>Damascus, MD 20715</address>

    <div class="divider"></div>

    <ul class="contacts">
      <li>
        <svg viewBox="0 0 16 16" aria-hidden="true"><circle cx="8" cy="8" r="8" fill="var(--ink-soft)"/><path d="M5.2 4.2l1.5 1.6-.8 1.1c.5 1.1 1.3 1.9 2.4 2.4l1.1-.8 1.6 1.5-.9 1.3C7.6 11.1 4.9 8.4 4 5.1z" fill="var(--card-red)"/></svg>
        <span>240.318.6624</span>
      </li>
      <li>
        <svg viewBox="0 0 16 16" aria-hidden="true"><circle cx="8" cy="8" r="8" fill="var(--ink-soft)"/><rect x="5.5" y="3.5" width="5" height="9" rx="1" fill="var(--card-red)"/><rect x="6.5" y="5" width="3" height="5" fill="var(--ink-soft)"/></svg>
        <span>703.581.4096</span>
      </li>
      <li>
        <svg viewBox="0 0 16 16" aria-hidden="true"><circle cx="8" cy="8" r="8" fill="var(--ink-soft)"/><rect x="4" y="5.2" width="8" height="5.6" fill="var(--card-red)"/><path d="M4.3 5.5L8 8.3l3.7-2.8" stroke="var(--ink-soft)" stroke-width="0.9" fill="none"/></svg>
        <span>carl@moltravex.com</span>
      </li>
    </ul>

    <p class="website">www.moltravex.com</p>
  </article>
</main>
</body>
</html>
```